Guaranteed Job - Sleek Sexy Business Card UV Spot

Im looking for a sleek and sexy business card, that resembles elite or VIP status status.
our business is corinvale.example
you can view our products on there, but our main audience for handing out our cards will be for people in the hospitality industry, so it will need to impress high management and CEO of hotels and restaurants, bars, clubs etc...
the card features will have UV spot on both sides, 400gsm stock. standard size.
Artwork should be 86 x 54mm + 2mm bleed = 90 x 58mm
it should have a nice "unique" uv spot pattern that highlights the card, not a repeated pattern, theres no originality there, and it will be disregarded.
The written material will be:
Corin Vale Hospitality College (logo)
Tobin Marsh
Director
Phone: 1300 615 737
Mobile: 0455 817 296
Email: info@corinvale.example
website: www.corinvale.example
I'm looking for originality here, i don't want just a simple stock card, want something that has a wow factor for people.
You will find the logo attached. you may invert the white to black words to suit the background as you please.
thank you and good luck
As a side note, ive received a lot of proposals, im too busy to give feedback to each and every one, so if i havent provided feedback for your design within 24 hours, then consider it not acceptable, and you could resubmit another design.
So far i have not seen any design that stood out for me, they all seem pretty generic. there nothing thats unique, i would figure for the amount that im offering, that people would put some more effort and creativity into the design.
so far over 200 designs submitted, and nothing i have seen looks very original, everything looks like a different variation of the same stuff, i said it very clearly i wanted something unique, the only thing that has come close to it so far is this one
Reason: Ive received alot of design concepts and i have reviewed everyone, but i havent had time to give feedback to every single one, only the ones that have interested me, if i havent responded, its because i havent found it good enough.
so far only a few design have been on par with what ive been looking for, an attractive eye popping design.
heres a few of them,
http://files.pixelbazaar.example/design_img/51736/62418/62418_2840915_51736_image.jpg
http://files.pixelbazaar.example/design_img/51736/68254/68254_2841377_51736_image.jpg
theyre, both unique and original, and eye catching, the only thing theyre missing is the sexyness.
if you still think you have some creativity left in your minds, then throw it on here.
Reason: Sorry guys for the delay, I was in a serious accident and out of commission for the past few months, I'm just slowly recovering now, please bare with me as i try to attend to this project, it may take me awhile as I have other projects that are on standby, I'm not 100% at the moment, so im extending the deadline for 2 weeks right now. Thanks for your patience.
Hospitality

```html
<!DOCTYPE html>
<html lang="en">
<head>
<meta charset="utf-8">
<title>Corin Vale Hospitality College – Business Card</title>
<link rel="stylesheet" href="https://fonts.googleapis.com/css2?family=Arvo:wght@700&display=swap">
<style>
  :root {
    --frame: #464f51;
    --card-dark: #1c1e21;
    --card-mid: #2b2e32;
    --blue-deep: #0b1d7a;
    --blue-bright: #2f6cff;
    --blue-light: #7cc4ff;
    --name-blue: #5cc3ec;
    --text-white: #ffffff;
    --text-grey: #c9d1d5;
  }
  * { margin: 0; padding: 0; box-sizing: border-box; }
  html, body {
    width: 1200px;
    height: 773px;
    overflow: hidden;
    background: var(--frame);
  }
  .card {
    position: absolute;
    left: 27px;
    top: 27px;
    width: 1147px;
    height: 720px;
    overflow: hidden;
    background: linear-gradient(100deg, var(--card-dark) 0%, var(--card-mid) 35%, var(--card-dark) 60%, var(--card-mid) 85%, var(--card-dark) 100%);
    font-family: "Arvo", "Rockwell", serif;
  }
  .streak-band {
    position: absolute;
    left: 0;
    width: 100%;
    background: linear-gradient(90deg, var(--blue-deep) 0%, var(--blue-bright) 25%, var(--blue-deep) 45%, var(--blue-light) 60%, var(--blue-bright) 80%, var(--blue-deep) 100%);
  }
  .streak-band--top { top: 0; height: 75px; }
  .streak-band--bottom { bottom: 0; height: 73px; }
  .divider {
    position: absolute;
    right: 0;
    height: 16px;
    background: linear-gradient(90deg, var(--blue-bright) 0%, var(--blue-light) 40%, var(--blue-bright) 70%, var(--blue-deep) 100%);
  }
  .divider--upper { top: 230px; left: 787px; }
  .divider--lower { top: 432px; left: 703px; }

  .brand {
    position: absolute;
    left: 50px;
    top: 290px;
    display: flex;
    align-items: center;
    gap: 40px;
  }
  .brand__square {
    width: 150px;
    height: 150px;
    background: var(--name-blue);
  }
  .brand__name {
    color: var(--text-white);
    font-weight: 700;
    line-height: 1.1;
  }
  .brand__name-main { display: block; font-size: 58px; }
  .brand__name-sub { display: block; font-size: 26px; letter-spacing: 1px; }

  .contact {
    position: absolute;
    right: 23px;
    text-align: right;
    font-weight: 700;
    white-space: nowrap;
  }
  .contact__name { top: 110px; font-size: 41px; color: var(--name-blue); }
  .contact__title { top: 161px; font-size: 26px; color: var(--text-white); }
  .contact__phone { top: 288px; font-size: 25px; color: var(--text-white); }
  .contact__mobile { top: 350px; font-size: 25px; color: var(--text-white); }
  .contact__email { top: 502px; font-size: 24px; color: var(--text-white); }
  .contact__web { top: 562px; font-size: 24px; color: var(--text-grey); }
</style>
</head>
<body>
  <div class="card">
    <div class="streak-band streak-band--top" role="img" aria-label="Blue light-streak texture band"></div>

    <div class="brand">
      <div class="brand__square"></div>
      <div class="brand__name">
        <span class="brand__name-main">CORIN VALE</span>
        <span class="brand__name-sub">HOSPITALITY COLLEGE</span>
      </div>
    </div>

    <div class="contact contact__name">Tobin Marsh</div>
    <div class="contact contact__title">Director</div>

    <div class="divider divider--upper"></div>

    <div class="contact contact__phone">Phone: 1300 615 737</div>
    <div class="contact contact__mobile">Mobile: 0455 817 296</div>

    <div class="divider divider--lower"></div>

    <div class="contact contact__email">info@corinvale.example</div>
    <div class="contact contact__web">www.corinvale.example</div>

    <div class="streak-band streak-band--bottom" role="img" aria-label="Blue light-streak texture band"></div>
  </div>
</body>
</html>
```